I have a website called Quellmark Estates (quellmarkestates.com) that I would like to have redesigned. Most of the content is already created, but I need a new design. You can also see my other website at dovanholdings.com. I am open to a new logo or modifying the current logo if you have a good idea. Please feel free to use other images for the home page (and maybe some other locations) if you feel they provide a better look and feel to the website. I prefer a modern look.

Important: You do not have to use the images I've provided for the home page. Feel free to find your own stock photos. You don't have to pay for them unless I select your design.

1) Please use wix.com to make your changes so that I can edit it later.
2) I will need all the graphics files to be saved so I can dowload it for later.
3) I will be adding more content to the site later.
4) This site will likely be transferred over to dovanholdings.com so if you make a logo please make one for Quellmark Estates and one for Dovan Holdings.
5) You can use other images that you feel would help the look and feel of the website.

Real Estate

```html
<!DOCTYPE html>
<html lang="en">
<head>
<meta charset="utf-8">
<title>Quellmark Estates</title>
<link rel="stylesheet" href="https://fonts.googleapis.com/css2?family=Lato:wght@400;700;900&display=swap">
<style>
:root{
  --navy:#0f3457;
  --ink:#2b4e6e;
  --blue:#3c6da3;
  --sky:#5b92d0;
  --slate:#2c4866;
  --text:#333;
  --muted:#777;
  --line:#e3e3e3;
}
*{box-sizing:border-box;margin:0;padding:0}
html,body{width:1200px;height:3896px;overflow:hidden;background:#fff;font-family:'Lato',sans-serif;color:var(--text)}
.page{position:relative;width:1200px;height:3896px}
.abs{position:absolute}
.brand{left:143px;top:14px;display:flex;align-items:center;gap:16px}
.brand-mark{width:40px;height:40px;background:var(--blue)}
.brand-name{font-size:32px;font-weight:700;color:var(--blue)}
.nav{left:578px;top:35px;display:flex;gap:29px;font-size:13px;color:#333;letter-spacing:.2px}
.nav .active{color:var(--sky)}
.hero{left:32px;top:86px;width:1134px;height:539px;background:linear-gradient(180deg,#4d5d78 0%,#6c7a8e 45%,#5a4a3e 80%,#3a3530 100%)}
.hero-title{left:139px;top:266px;font-size:62px;font-weight:900;line-height:70px;color:#fff;letter-spacing:-1px}
.btn{display:flex;align-items:center;justify-content:center;background:var(--navy);color:#fff;font-weight:700;font-size:15px}
.side-social{left:1174px;width:14px;height:14px;border-radius:50%;background:#222}
.section-title{left:0;width:1200px;text-align:center;font-size:52px;font-weight:900;color:var(--ink)}
.section-title span{color:var(--blue)}
.card{top:784px;width:262px;height:358px;border:1px solid var(--line);box-shadow:0 1px 4px rgba(0,0,0,.08);background:#fff}
.card-img{margin:9px;height:154px}
.card h3{font-size:19px;font-weight:700;color:#333;margin:20px 18px 8px;white-space:nowrap}
.card ul{list-style:none;margin:0 20px;font-size:11.5px;line-height:20px;color:var(--muted)}
.about-photo{left:30px;top:1294px;width:1136px;height:529px;background:linear-gradient(90deg,#6f8494 0%,#3e4f66 35%,#5d6f5a 60%,#7f8f80 100%)}
.about-panel{left:667px;top:1294px;width:385px;height:529px;background:var(--sky);color:#fff;padding:56px 32px 0 32px}
.about-panel h2{font-size:52px;font-weight:900;line-height:60px;margin-bottom:20px}
.about-panel p{font-size:13.5px;line-height:24px;text-align:justify}
.more{display:inline-block;margin-top:26px;font-size:14px;text-decoration:underline;color:#fff}
.intro{left:250px;top:1972px;width:700px;text-align:center;font-size:12px;line-height:21px;color:var(--muted)}
.grid{left:32px;top:2138px;width:1134px;height:458px;display:grid;grid-template-columns:repeat(4,1fr);grid-template-rows:repeat(2,1fr)}
.offer-photo{left:30px;top:2627px;width:1136px;height:529px;background:linear-gradient(180deg,#6f9ad0 0%,#b9c8d8 45%,#d8cfc0 75%,#6c6a4e 100%)}
.offer-panel{left:143px;top:2627px;width:384px;height:529px;background:var(--slate);color:#fff;padding:36px 32px 0 32px}
.offer-panel h2{font-size:50px;font-weight:900;line-height:46px;margin-bottom:28px}
.offer-panel p{font-size:13px;line-height:24px}
.foot-col{top:3212px}
.foot-col h4{font-size:17px;font-weight:700;color:#333;letter-spacing:.3px}
.foot-col .bar{width:32px;height:3px;background:var(--sky);margin:12px 0 20px}
.foot-col ul{list-style:none;font-size:13px;line-height:25.5px;color:#333}
.contact li{display:flex;gap:18px}
.contact svg{flex:none;margin-top:7px}
.social-dot{width:26px;height:26px;border-radius:50%}
.rule{left:38px;width:1120px;height:1px;background:var(--line)}
.join{left:0;top:3512px;width:1200px;text-align:center;font-size:30px;font-weight:700;color:#333}
.field{border:1px solid #bbb;font-size:13px;color:#444;padding:13px 26px}
.copy{left:0;top:3836px;width:1200px;text-align:center;font-size:12.5px;color:#333}
</style>
</head>
<body>
<div class="page">

  <header>
    <div class="abs brand"><div class="brand-mark"></div><div class="brand-name">Quellmark Estates</div></div>
    <nav class="abs nav">
      <span class="active">HOME</span><span>STRATEGY</span><span>ABOUT US</span><span>CURRENT OFFERINGS</span><span>CONTACT</span>
    </nav>
  </header>

  <section>
    <div class="abs hero" role="img" aria-label="Modern brick and glass apartment building against an overcast sky"></div>
    <h1 class="abs hero-title">BUILDING TOGETHER.<br>GROWING TOGETHER.</h1>
    <div class="abs btn" style="left:140px;top:433px;width:147px;height:40px">GET STARTED</div>
    <div class="abs side-social" style="top:250px"></div>
    <div class="abs side-social" style="top:297px"></div>
    <div class="abs side-social" style="top:344px"></div>
  </section>

  <section>
    <h2 class="abs section-title" style="top:682px">Our <span>Strategy</span></h2>
    <div class="abs card" style="left:32px">
      <div class="card-img" role="img" aria-label="Red brick apartment complex" style="background:linear-gradient(180deg,#7da3d6,#a0403c 60%,#6e8a4c)"></div>
      <h3>Investment Focus</h3>
      <ul><li>Development</li><li>Value-Add Acquisition</li><li>Debt Financing</li></ul>
    </div>
    <div class="abs card" style="left:322px">
      <div class="card-img" role="img" aria-label="Rendering of a modern mixed-use building" style="background:linear-gradient(180deg,#c9d3dc,#54514e 60%,#8b9a7e)"></div>
      <h3>Role of Dovan Holdings</h3>
      <ul><li>Opportunity Procurement</li><li>Financial Underwriting</li><li>Capital Raising</li><li>Due Diligence</li><li>Asset Management</li><li>Disposition</li></ul>
    </div>
    <div class="abs card" style="left:612px">
      <div class="card-img" role="img" aria-label="Evening courtyard with lit trees and pool" style="background:linear-gradient(90deg,#2d3b4e,#5f6f52 60%,#b9a85a)"></div>
      <h3>Preferred Markets</h3>
      <ul><li>Primary: Texas</li><li>Secondary: Southern U.S.</li></ul>
    </div>
    <div class="abs card" style="left:903px">
      <div class="card-img" role="img" aria-label="Architectural elevation drawing" style="background:linear-gradient(180deg,#f2f2f2,#d6d6d6)"></div>
      <h3>Deal Structure</h3>
      <ul><li>Project terms will be evaluated on a</li><li>deal-by-deal basis.</li></ul>
    </div>
    <div class="abs btn" style="left:525px;top:1196px;width:147px;height:41px">VIEW ALL</div>
  </section>

  <section>
    <div class="abs about-photo" role="img" aria-label="Three company partners standing outdoors in front of city buildings"></div>
    <div class="abs about-panel">
      <h2>About Us</h2>
      <p>Dovan Holdings is a private real estate firm that specializes in the procurement, development, management, and disposition of various commercial real estate asset types including multifamily, hospitality, industrial and self-storage. The firm effectuates its strategy by providing procuring and developing projects which provide a strong risk-adjusted return their accredited investors, institutional funds, private equity funds, and family offices. Dovan Holdings specifically targets development and value-add projects in Texas and other major metropolitan areas in the southern region of the U.S.</p>
      <span class="more">MORE</span>
    </div>
  </section>

  <section>
    <h2 class="abs section-title" style="top:1899px">Our <span>Projects</span></h2>
    <p class="abs intro">This is your Project Page. It's a great opportunity to help visitors understand the context and background of your latest work. Double click on the text box to start editing your content and make sure to add all the relevant details you want to share.</p>
    <div class="abs btn" style="left:525px;top:2045px;width:147px;height:39px">VIEW ALL</div>
    <div class="abs grid">
      <div role="img" aria-label="Beige apartment complex with landscaped drive" style="background:linear-gradient(180deg,#b8cde0,#c8b89a 55%,#6e7b55)"></div>
      <div role="img" aria-label="Rendering of a modern apartment community" style="background:linear-gradient(180deg,#e6edf3,#6b5a4e 55%,#7f9a5c)"></div>
      <div role="img" aria-label="White industrial building under blue sky" style="background:linear-gradient(180deg,#2d6fcf,#e9ecef 60%,#9aa0a4)"></div>
      <div role="img" aria-label="Modern townhomes with red doors" style="background:linear-gradient(180deg,#8fb2d9,#d9d2c6 55%,#8b8b8b)"></div>
      <div role="img" aria-label="Apartment entrance sign with landscaping" style="background:linear-gradient(180deg,#8fb9e6,#4b5c64 55%,#5e7a3e)"></div>
      <div role="img" aria-label="Red brick apartment complex" style="background:linear-gradient(180deg,#7da3d6,#a0403c 60%,#6e8a4c)"></div>
      <div role="img" aria-label="Hotel facade at dusk" style="background:linear-gradient(180deg,#1d3fb0,#a07a66 60%,#4e3a32)"></div>
      <div role="img" aria-label="Hotel building lit at dusk" style="background:linear-gradient(180deg,#2a4fb8,#b59a80 60%,#5a4636)"></div>
    </div>
  </section>

  <section>
    <div class="abs offer-photo" role="img" aria-label="White high-rise residential tower with Mediterranean-style buildings"></div>
    <div class="abs offer-panel">
      <h2>Current<br>Offerings</h2>
      <p>Investment Highlights<br>20% IRR with a 3x multiple on a 7-year proforma<br>HUD Loan – 3.5% Rate, 40 Year Amortization, 85% Loan-to-Value<br>Property Tax is one of the lowest in the metroplex<br>Entitlement and zoning work provides a great long-term strategy<br>Population and job growth in the area is unprecedented<br>The site is located on Harlow Road which has over 19,000 car trips per day and is adjacent to I-42 which has 120,000 car trips per day.</p>
      <span class="more">MORE</span>
    </div>
  </section>

  <footer>
    <div class="abs foot-col" style="left:146px">
      <h4>QUICK LINKS</h4><div class="bar"></div>
      <ul><li>Home</li><li>Strategy</li><li>About us</li><li>Current offerings</li><li>Contact</li></ul>
    </div>
    <div class="abs foot-col" style="left:356px">
      <h4>OTHER LINKS</h4><div class="bar"></div>
      <ul><li>Privacy Policy</li><li>Terms and Use</li><li>Sitemap</li><li>Information</li><li>Blog</li></ul>
    </div>
    <div class="abs foot-col" style="left:589px">
      <h4>CONTACT INFO</h4><div class="bar"></div>
      <ul class="contact">
        <li><svg width="16" height="12" viewBox="0 0 16 12"><path d="M0 2l5-2 6 2 5-2v10l-5 2-6-2-5 2z" fill="#2b4e6e"/></svg><span>4870 Calloway Ave. 9th Floor<br>Marlow, Texas 75388</span></li>
        <li><svg width="16" height="12" viewBox="0 0 16 12"><rect width="16" height="12" fill="#2b4e6e"/><path d="M0 0l8 6 8-6" stroke="#fff" fill="none"/></svg><span>info@dovanholdings.com</span></li>
        <li><svg width="16" height="12" viewBox="0 0 16 16"><path d="M3 1l3 3-2 2c1 2 3 4 6 6l2-2 3 3-2 2C7 15 1 9 1 3z" fill="#2b4e6e"/></svg><span>Tel: (555) 214-0973</span></li>
      </ul>
    </div>
    <div class="abs foot-col" style="left:926px">
      <h4>SOCIAL MEDIA</h4><div class="bar"></div>
      <div style="display:flex;gap:6px;margin-top:-4px">
        <div class="social-dot" style="background:#3b66c4"></div>
        <div class="social-dot" style="background:#0f3457"></div>
      </div>
    </div>

    <div class="abs rule" style="top:3455px"></div>
    <h2 class="abs join">JOIN OUR COMMUNITY</h2>
    <div class="abs field" style="left:347px;top:3585px;width:246px;height:44px">Enter Name</div>
    <div class="abs field" style="left:604px;top:3585px;width:246px;height:44px">Email Address</div>
    <div class="abs field" style="left:347px;top:3639px;width:503px;height:76px">Message</div>
    <div class="abs btn" style="left:347px;top:3727px;width:503px;height:42px">SEND MESSAGE</div>
    <div class="abs rule" style="top:3799px"></div>
    <p class="abs copy">Copyright © Quellmark Estates. 2022 All rights reserved. &nbsp;|&nbsp; Privacy policy</p>
  </footer>

</div>
</body>
</html>
```